KT Crewing business card

Require business card which includes:
Company name: KT CREWING PTY LTD
Email: Mick@ktcrewing.com.au
Phone: 0431 556 208
ACN: 517 238 649

slogan: Onsite Auto Electrician Labour hire

Details and logo on top side
Logo only on bottom side

colour codes : #F15A29 , #939598

Target Market(s)

Western Australia mining sector

Industry/Entity Type

Mining

Contact Information for Business Card

Require business card which includes: Company name: KT CREWING PTY LTD Email: Mick@ktcrewing.com.au Phone: 0431 556 208 ACN: 517 238 649 slogan: Onsite Auto Electrician Labour hire Details and logo on top side Logo only on bottom side colour codes : #F15A29 , #939598

Colors
EE7325
F08F49
F5BC92
FAE3D3
FDF4ED

Requirements
Must have
• double sided

```html
<!DOCTYPE html>
<html lang="en">
<head>
<meta charset="utf-8">
<title>KT Crewing – Business Card</title>
<link rel="stylesheet" href="https://fonts.googleapis.com/css2?family=Montserrat:wght@400;500;800&family=Oswald:wght@600&display=swap">
<style>
  :root {
    --brand-orange: #F15A29;
    --orange-deep: #E8522A;
    --orange-light: #F5BC92;
    --white: #FFFFFF;
    --backdrop: #2A2A2E;
  }
  * { box-sizing: border-box; margin: 0; padding: 0; }
  html, body { width: 1200px; height: 817px; overflow: hidden; }
  body {
    background: var(--backdrop);
    font-family: "Montserrat", sans-serif;
    color: var(--white);
    position: relative;
  }
  .card {
    position: absolute;
    width: 560px;
    height: 320px;
    background: var(--brand-orange);
    border-radius: 24px;
    overflow: hidden;
  }
  .card--front { left: 40px; top: 60px; }
  .card--back { left: 600px; top: 437px; }

  .circuit-area {
    position: absolute;
    background: linear-gradient(135deg, rgba(245,188,146,0.05), rgba(245,188,146,0.28));
  }
  .card--front .circuit-area {
    right: 0; top: 0; width: 300px; height: 170px;
    border-bottom-left-radius: 120px;
  }
  .card--back .circuit-area--left {
    left: 0; bottom: 0; width: 200px; height: 230px;
    border-top-right-radius: 120px;
    background: linear-gradient(45deg, rgba(245,188,146,0.28), rgba(245,188,146,0.05));
  }
  .card--back .circuit-area--right {
    right: 0; top: 30px; width: 80px; height: 150px;
    border-bottom-left-radius: 60px;
  }

  .wordmark {
    display: flex;
    align-items: center;
    gap: 12px;
    font-family: "Montserrat", sans-serif;
    font-weight: 800;
    color: var(--white);
    line-height: 1;
  }
  .wordmark__square {
    background: var(--white);
    flex: none;
  }
  .card--front .wordmark { position: absolute; left: 40px; top: 62px; font-size: 44px; }
  .card--front .wordmark__square { width: 22px; height: 22px; }

  .details { position: absolute; left: 40px; top: 150px; }
  .details__company {
    font-family: "Oswald", sans-serif;
    font-weight: 600;
    font-size: 24px;
    letter-spacing: 0.5px;
    margin-bottom: 8px;
  }
  .details__acn { font-size: 16px; font-weight: 400; margin-bottom: 12px; }
  .details__acn strong { font-weight: 500; }
  .contact { list-style: none; font-size: 14px; }
  .contact li { display: flex; align-items: center; gap: 10px; margin-bottom: 8px; }
  .contact svg { width: 18px; height: 18px; flex: none; }

  .card--back .brand-block {
    position: absolute; left: 0; right: 0; top: 100px;
    display: flex; flex-direction: column; align-items: center;
  }
  .card--back .wordmark { font-size: 52px; }
  .card--back .wordmark__square { width: 26px; height: 26px; }
  .slogan {
    margin-top: 34px;
    font-size: 13px;
    font-weight: 500;
    letter-spacing: 1px;
    text-transform: uppercase;
  }
</style>
</head>
<body>
  <section class="card card--front" aria-label="Card front">
    <div class="circuit-area" role="img" aria-label="Light circuit-line pattern with round nodes"></div>
    <div class="wordmark"><span class="wordmark__square"></span>KT Crewing</div>
    <div class="details">
      <p class="details__company">KT CREWING PTY LTD</p>
      <p class="details__acn"><strong>ACN:</strong> 517 238 649</p>
      <ul class="contact">
        <li>
          <svg viewBox="0 0 18 18" aria-hidden="true"><circle cx="9" cy="9" r="9" fill="#fff"/><path d="M6 4.5l1.6 2.2-1 1.2a6 6 0 0 0 3.5 3.5l1.2-1 2.2 1.6-.8 1.6c-3.9-.2-7.3-3.6-7.5-7.5z" fill="#F15A29"/></svg>
          0431 556 208
        </li>
        <li>
          <svg viewBox="0 0 18 18" aria-hidden="true"><circle cx="9" cy="9" r="9" fill="#fff"/><rect x="4.5" y="6" width="9" height="6.5" rx="0.8" fill="#F15A29"/><path d="M4.8 6.4L9 9.6l4.2-3.2" stroke="#fff" stroke-width="0.9" fill="none"/></svg>
          Mick@ktcrewing.com.au
        </li>
      </ul>
    </div>
  </section>

  <section class="card card--back" aria-label="Card back">
    <div class="circuit-area circuit-area--left" role="img" aria-label="Light circuit-line pattern with round nodes"></div>
    <div class="circuit-area circuit-area--right" role="img" aria-label="Light circuit-line pattern with round nodes"></div>
    <div class="brand-block">
      <div class="wordmark"><span class="wordmark__square"></span>KT Crewing</div>
      <p class="slogan">Onsite Auto Electrician Labour Hire</p>
    </div>
  </section>
</body>
</html>
```